Velmora Partners - website for real estate investment company

Create a bold, modern website that reflects Velmora’s success, professionalism, and credibility.
The design must stand out while maintaining a polished, corporate tone. (bold, but understated)
The client just created a new logo, and the website design must be in sync with the logo design. Information about the logo colors, fonts, and message are in the attached design brief.
Updates

Target Market(s)

b2b: banks, brokers, institutional partners, vendors, and property sellers.

Industry/Entity Type

real estate investment company

Number of Pages Required

1 page

Font styles to use
Sans Serif

Colors

Designer to choose colors to be used in the design.

Requirements
Must have
• 1. homepage design (psd) 2. a top banner image (psd) for a default inner page
Nice to have
• please see attached design brief
Should not have

```html
<!DOCTYPE html>
<html lang="en">
<head>
<meta charset="utf-8">
<title>Velmora Partners</title>
<link href="https://fonts.googleapis.com/css2?family=Poppins:wght@400;500;600;700&family=Barlow+Semi+Condensed:wght@600;700&display=swap" rel="stylesheet">
<style>
:root{
  --red:#dd1f26;
  --red-soft:#e2545a;
  --ink:#111111;
  --grey:#4a4a4a;
  --mid:#555555;
  --footer-bg:#efefef;
  --line:#dcdcdc;
  --white:#ffffff;
}
*{box-sizing:border-box;margin:0;padding:0}
html,body{width:1200px;height:2951px;overflow:hidden;background:var(--white)}
body{position:relative;font-family:'Poppins',sans-serif;color:var(--ink)}
.abs{position:absolute}
.brand{font-family:'Poppins',sans-serif;font-weight:700;color:var(--grey);letter-spacing:1px;white-space:nowrap}

/* header */
.site-header{position:absolute;left:0;top:0;width:1200px;height:125px;background:var(--white)}
.site-header .brand{left:66px;top:24px;font-size:54px;line-height:76px}
.main-nav a{position:absolute;top:51px;font-size:14px;line-height:20px;color:var(--ink);text-decoration:none;white-space:nowrap}
.main-nav a.active{color:var(--red);font-weight:600}
.btn-contact{position:absolute;left:964px;top:37px;width:172px;height:51px;border-radius:26px;background:var(--red);color:var(--white);font-weight:600;font-size:15px;display:flex;align-items:center;justify-content:center}

/* hero */
.hero{position:absolute;left:0;top:125px;width:1200px;height:670px}
.hero-copy{position:absolute;left:0;top:80px;width:1200px;text-align:center}
.hero-copy h1{font-family:'Barlow Semi Condensed',sans-serif;font-weight:700;font-size:56px;letter-spacing:1px;color:var(--ink)}
.hero-copy p{font-size:14.5px;line-height:22px;margin:10px auto 0;width:760px;color:var(--ink)}
.hero-mark{position:absolute;left:0;top:235px;width:1200px;text-align:center;font-size:150px;line-height:150px;color:rgba(120,120,120,.22)}

/* section heading */
.section-title{position:absolute;left:0;width:1200px;text-align:center;font-family:'Barlow Semi Condensed',sans-serif;font-weight:700;font-size:42px;color:var(--grey);letter-spacing:1px}
.section-rule{position:absolute;left:549px;width:106px;height:3px;background:var(--grey)}

/* stat cards */
.stat{position:absolute;top:1037px;width:296px;height:584px}
.stat svg.peak{position:absolute;left:0;top:0}
.stat .icon{position:absolute;left:118px;top:49px}
.stat .figure{position:absolute;left:0;top:122px;width:296px;text-align:center;color:var(--white);font-size:28px;font-weight:500}
.stat .photo{position:absolute;left:0;top:192px;width:296px;height:392px}
.stat .band{position:absolute;left:0;width:296px;height:90px;background:rgba(0,0,0,.55)}
.stat .band-tri{position:absolute;left:0}
.stat .label{position:absolute;left:40px;right:10px;height:90px;display:flex;align-items:center;justify-content:center;text-align:center;color:var(--white);font-weight:600;font-size:21px;line-height:22px}

/* form */
.field{position:absolute;height:45px;background:var(--white);box-shadow:0 1px 8px rgba(0,0,0,.12);font-size:13px;color:#888;padding:0 20px;display:flex;align-items:center}
.field.msg{align-items:flex-start;padding-top:22px}
.btn-submit{position:absolute;left:70px;top:2207px;width:154px;height:50px;border-radius:6px;background:var(--red);color:var(--white);font-weight:600;font-size:16px;display:flex;align-items:center;justify-content:center}

/* footer */
.footer-bg{position:absolute;left:0;top:2380px;width:1200px;height:571px}
.footer-brand{left:125px;top:2640px;font-size:56px;line-height:80px}
.social{position:absolute;top:2735px;width:37px;height:37px;border-radius:50%;background:var(--red)}
.col-title{position:absolute;font-family:'Barlow Semi Condensed',sans-serif;font-weight:600;font-size:25px;color:var(--red);letter-spacing:.5px}
.col-rule{position:absolute;width:96px;height:1px;background:#bbb}
.links{position:absolute;left:520px;top:2663px;list-style:none;font-size:14.5px}
.links li{height:32.5px;padding-left:22px;position:relative}
.links li::before{content:"";position:absolute;left:1px;top:7px;width:7px;height:7px;border-radius:50%;background:var(--red)}
.contact-item{position:absolute;left:822px;display:flex;align-items:center;font-size:14.5px;line-height:21px}
.contact-item .badge{width:37px;height:37px;border-radius:50%;background:var(--red);flex:none;margin-right:14px;display:flex;align-items:center;justify-content:center}
.footer-rule{position:absolute;left:70px;top:2860px;width:1062px;height:1px;background:var(--line)}
.copyright{position:absolute;left:0;top:2886px;width:1200px;text-align:center;font-size:15px}
</style>
</head>
<body>

<header class="site-header">
  <div class="abs brand">VELMORA</div>
  <nav class="main-nav">
    <a class="active" href="#" style="left:371px">Home</a>
    <a href="#" style="left:441px">Our Story</a>
    <a href="#" style="left:526px">Investment Strategy</a>
    <a href="#" style="left:696px">What Sets Us Apart</a>
    <a href="#" style="left:855px">Our Portfolio</a>
  </nav>
  <div class="btn-contact">CONTACT US</div>
</header>

<section class="hero">
  <svg class="abs" style="left:0;top:0" width="1200" height="670" role="img" aria-label="Aerial view of a city skyline with skyscrapers at sunset">
    <defs>
      <linearGradient id="sky" x1="0" y1="0" x2="0" y2="1">
        <stop offset="0" stop-color="#e9eef3"/>
        <stop offset=".35" stop-color="#f3f1ec"/>
        <stop offset=".55" stop-color="#b7a993"/>
        <stop offset=".75" stop-color="#5c4f43"/>
        <stop offset="1" stop-color="#2f2b29"/>
      </linearGradient>
    </defs>
    <polygon points="0,0 1200,0 1200,525 600,640 0,525" fill="url(#sky)"/>
    <polygon points="0,525 600,640 1200,525 1200,530 600,665 0,535" fill="var(--red)"/>
    <polygon points="0,0 190,0 0,190" fill="var(--red-soft)"/>
  </svg>
  <div class="hero-mark brand">VELMORA</div>
  <div class="hero-copy">
    <h1>EXPERIENCE – STRATEGY – VISION</h1>
    <p>Velmora Partners is a vertically integrated real estate investment firm with a proven<br>four-decade track record. We acquire, reposition, and operate high-performing assets across multiple<br>sectors — always with a focus on exceptional, risk-adjusted returns.</p>
  </div>
  <svg class="abs" style="left:559px;top:394px" width="56" height="56">
    <circle cx="28" cy="28" r="25" fill="none" stroke="#fff" stroke-width="3"/>
    <polygon points="22,16 40,28 22,40" fill="#fff"/>
  </svg>
</section>

<h2 class="section-title" style="top:895px">VITAL STATS</h2>
<div class="section-rule" style="top:955px"></div>

<div class="stat" style="left:70px">
  <svg class="peak" width="296" height="180"><polygon points="0,118 60,118 0,178" fill="var(--grey)"/><polygon points="146,0 296,176 0,176" fill="var(--red)"/></svg>
  <svg class="icon" width="56" height="62" fill="none" stroke="#fff" stroke-width="3"><path d="M28 58 C12 42 6 32 6 24 A22 22 0 0 1 50 24 C50 32 44 42 28 58Z"/><circle cx="28" cy="24" r="13"/><path d="M21 24l5 5 9-9"/></svg>
  <div class="figure">1989</div>
  <div class="photo" role="img" aria-label="Honeycomb-like architectural structure among glass towers and trees" style="background:linear-gradient(180deg,#a9bfd1 0%,#8a6a52 35%,#6b5444 55%,#3f5a33 80%,#2c3f24 100%)"></div>
  <div class="band" style="top:348px"></div>
  <svg class="band-tri" style="top:348px" width="80" height="90"><polygon points="0,0 80,0 0,90" fill="var(--red)" opacity=".8"/></svg>
  <div class="label" style="top:348px">FOUNDED</div>
</div>

<div class="stat" style="left:452px">
  <svg class="peak" width="296" height="180"><polygon points="0,118 60,118 0,178" fill="var(--grey)"/><polygon points="146,0 296,176 0,176" fill="var(--red)"/></svg>
  <svg class="icon" width="60" height="56" fill="none" stroke="#fff" stroke-width="3"><circle cx="32" cy="24" r="16"/><path d="M32 16v16M24 24h16"/><path d="M4 40c8-4 14-2 20 2h12M4 50c10 2 22 2 34-6"/></svg>
  <div class="figure">23,000+</div>
  <div class="photo" role="img" aria-label="Brick apartment building with courtyard lawn and paved path" style="background:linear-gradient(180deg,#7fb1c4 0%,#8a7668 35%,#6a5c50 55%,#6b7c46 80%,#8f8c80 100%)"></div>
  <div class="band" style="top:348px"></div>
  <svg class="band-tri" style="top:348px" width="80" height="90"><polygon points="0,0 80,0 0,90" fill="var(--red)" opacity=".8"/></svg>
  <div class="label" style="top:348px">MULTIFAMILY &amp;<br>HEALTHCARE UNITS</div>
</div>

<div class="stat" style="left:836px">
  <svg class="peak" width="296" height="180"><polygon points="0,118 60,118 0,178" fill="var(--grey)"/><polygon points="146,0 296,176 0,176" fill="var(--red)"/></svg>
  <svg class="icon" width="60" height="50" fill="none" stroke="#fff" stroke-width="3"><path d="M4 46h52M10 46V30h8v16M24 46V24h8v16M38 46V18h8v28"/><path d="M6 22l14-10 10 6 18-14"/></svg>
  <div class="figure">$300+</div>
  <div class="photo" role="img" aria-label="Glowing rising arrow chart above a tablet on a dark green background" style="background:radial-gradient(circle at 60% 40%,#1b5a48 0%,#0d2f27 45%,#050f0d 100%)"></div>
  <div class="band" style="top:348px"></div>
  <svg class="band-tri" style="top:348px" width="80" height="90"><polygon points="0,0 80,0 0,90" fill="var(--red)" opacity=".8"/></svg>
  <div class="label" style="top:348px">MILLION INVESTED<br>IN RENOVATIONS</div>
</div>

<h2 class="section-title" style="top:1757px">PERSISTENT FOOTER CONTACT</h2>
<div class="section-rule" style="top:1819px"></div>

<div class="field" style="left:74px;top:1903px;width:220px">First Name:</div>
<div class="field" style="left:315px;top:1903px;width:220px">Last Name:</div>
<div class="field" style="left:74px;top:1968px;width:220px">Phone:</div>
<div class="field" style="left:315px;top:1968px;width:220px">Email:</div>
<div class="field msg" style="left:74px;top:2034px;width:461px;height:140px">Mesage:</div>
<div class="btn-submit">SUBMIT NOW</div>

<div class="abs" role="img" aria-label="Colourful row of residential buildings with bay windows and flowering hydrangeas" style="left:602px;top:1894px;width:514px;height:383px;background:linear-gradient(160deg,#e7e9ec 0%,#c9cfd6 40%,#b98a6b 60%,#4e6a3a 85%,#8c8bbf 100%)"></div>
<svg class="abs" style="left:592px;top:1884px" width="178" height="186"><polygon points="0,0 178,0 0,186" fill="var(--red)" opacity=".75"/></svg>

<svg class="footer-bg" width="1200" height="571">
  <polygon points="0,150 602,12 1200,150 1200,571 0,571" fill="var(--footer-bg)"/>
  <polygon points="30,150 602,0 1170,150 602,22" fill="var(--red)"/>
</svg>

<div class="abs brand footer-brand">VELMORA</div>
<div class="social" style="left:184px" role="img" aria-label="Social profile"></div>
<div class="social" style="left:232px" role="img" aria-label="Social profile"></div>
<div class="social" style="left:279px" role="img" aria-label="Social profile"></div>

<div class="col-title" style="left:520px;top:2590px">LINKS</div>
<div class="col-rule" style="left:520px;top:2634px"></div>
<ul class="links">
  <li>Our Story</li>
  <li>Investment Strategy</li>
  <li>What Sets Us Apart</li>
  <li>Our Portfolio</li>
  <li>Contact</li>
</ul>

<div class="col-title" style="left:820px;top:2590px">CONTACT US</div>
<div class="col-rule" style="left:820px;top:2634px"></div>
<div class="contact-item" style="top:2663px">
  <span class="badge"><svg width="16" height="20"><path d="M8 19C3 13 1 10 1 7a7 7 0 0 1 14 0c0 3-2 6-7 12z" fill="#fff"/><circle cx="8" cy="7" r="2.5" fill="var(--red)"/></svg></span>
  <span>Lorem ipsum,Lorem ipsum.<br>Lorem ipsum</span>
</div>
<div class="contact-item" style="top:2723px">
  <span class="badge"><svg width="18" height="18"><path d="M4 1l3 4-2 2c1 2 3 4 5 5l2-2 4 3-2 3C8 16 2 10 1 4z" fill="#fff"/></svg></span>
  <span>(987) 654 3210</span>
</div>
<div class="contact-item" style="top:2777px">
  <span class="badge"><svg width="18" height="14"><rect x="1" y="1" width="16" height="12" fill="#fff"/><path d="M1 1l8 7 8-7" fill="none" stroke="var(--red)" stroke-width="1.5"/></svg></span>
  <span>info@velmora-example.com</span>
</div>

<div class="footer-rule"></div>
<div class="copyright">Copyright © 2025 All Rights Reserved By Company Name</div>

</body>
</html>
```